Landing page for a cyber security service provider called 'Quill Vantor'

The client is a new cyber security company in need of a website landing page at quillvantor.com.

Their visual identity is modern, playful, clean and uncluttered and represents innovation, connectivity and approachability.

The company logo is provided in black (attached) but the client is open to changing the colour to align with the new website design.

The landing page needs to contain:
- A call to action with a 'Get Started' button
-Links to blank 'How it works', 'Products', 'Pricing', 'About Us' and 'Contact Us' pages (that we'll fill out later)

Target Market(s)

Medium to large businesses who probably don't understand cyber / cyber security but need their business to be protected.

Industry/Entity Type

Cyber Security

Coding

Coded - Design and coding required

Number of Pages Required

1 page

Font styles to use
Sans Serif
Other font styles liked:
• Helvetica

Requirements
Nice to have
• Hero banner at the top of the landing page.
Should not have
• Should not look like a traditional cyber / cyber security design (eg no dark blue/ black, red/black colour combinations). Please no military styles (eg no shields, cannons, swords, guns)

```html
<!DOCTYPE html>
<html lang="en">
<head>
<meta charset="utf-8">
<title>Quill Vantor — Cyber Security</title>
<link href="https://fonts.googleapis.com/css2?family=Poppins:wght@300;400;500;600&display=swap" rel="stylesheet">
<style>
:root{
  --blue:#0b76c5;
  --blue-bright:#2e95e3;
  --sky:#5fb6f2;
  --ink:#1f2a36;
  --text:#4a5562;
  --muted:#7d8894;
  --footer:#1479c8;
  --footer-text:#e4f1fc;
  --pale:#f3f7fc;
  --wave:#e3ebf6;
  --line:#dde3ea;
  --orange:#f5a041;
  --white:#fff;
}
*{margin:0;padding:0;box-sizing:border-box}
html,body{width:1200px;height:4545px;overflow:hidden}
body{position:relative;font-family:"Poppins",Helvetica,Arial,sans-serif;color:var(--ink);background:var(--white)}
.abs{position:absolute}
a{color:inherit;text-decoration:none}

/* Hero */
.hero-art{position:absolute;left:0;top:0}
.brand{left:185px;top:60px;color:var(--white);font-size:22px;font-weight:500;letter-spacing:.5px;line-height:30px}
.brand-dot{display:inline-block;width:14px;height:14px;border-radius:50%;background:var(--white);margin-right:8px;vertical-align:-1px}
.topbar{left:675px;top:30px;display:flex;align-items:center;gap:14px;color:var(--white);font-size:13px}
.btn-quote{background:var(--white);color:var(--blue);font-weight:500;padding:8px 20px;font-size:14px;margin-left:18px}
.nav-rule{left:340px;top:90px;width:670px;height:1px;background:rgba(255,255,255,.35)}
.nav{left:360px;top:111px;display:flex;gap:40px;color:var(--white);font-size:15px}
.hero-kicker{left:187px;top:238px;color:var(--white);font-size:22px;font-weight:300}
.hero-title{left:186px;top:282px;color:var(--white);font-size:45px;line-height:62px;font-weight:600}
.hero-title .light{font-weight:300}
.btn-start{left:185px;top:433px;width:161px;height:46px;border-radius:23px;background:var(--white);color:var(--blue);font-size:15px;font-weight:600;display:flex;align-items:center;justify-content:center}

/* About */
.about-visual{left:88px;top:745px;width:442px;height:332px;background:radial-gradient(circle at 50% 55%,#eef2f6 0%,#fafbfc 70%,#fff 100%)}
.kicker{font-size:16px;color:var(--text)}
.about-kicker{left:604px;top:770px}
.about-title{left:603px;top:805px;font-size:36px;line-height:44px;font-weight:500}
.about-text{left:604px;top:913px;width:400px;font-size:12.5px;line-height:24px;color:var(--text)}
.btn{background:var(--blue);color:var(--white);font-size:13px;font-weight:500;display:flex;align-items:center;justify-content:center}
.about-btn{left:604px;top:1032px;width:123px;height:38px}

/* Provide */
.provide-bg{left:14px;top:1094px;width:1118px;height:803px;background:linear-gradient(180deg,#fbfcfe 0%,var(--pale) 60%,#eef3fa 100%)}
.section-head{width:1200px;left:0;text-align:center}
.section-head .label{font-size:13px;color:var(--text)}
.section-head h2{font-size:27px;font-weight:500;margin-top:4px}
.section-head .bar{width:50px;height:3px;background:var(--blue);margin:8px auto 0}
.hex-wrap{width:190px;height:218px;filter:drop-shadow(0 6px 14px rgba(30,70,120,.12))}
.hex{width:100%;height:100%;background:var(--white);clip-path:polygon(50% 0,100% 25%,100% 75%,50% 100%,0 75%,0 25%);display:flex;flex-direction:column;align-items:center;justify-content:center;color:var(--ink);font-size:13px;font-weight:500}
.hex svg{width:58px;height:58px;margin-bottom:16px;stroke:var(--blue);fill:none;stroke-width:2}
.hex .tick{width:40px;height:2px;background:var(--blue);margin-top:20px}
.hex.active{background:var(--blue);color:var(--white)}
.hex.active svg{stroke:var(--white)}
.hex.active .tick{background:var(--white)}

/* Services */
.service-title{display:flex;align-items:center;gap:18px;font-size:18px;line-height:22px;font-weight:500}
.service-title svg{width:52px;height:52px;stroke:var(--blue);fill:none;stroke-width:1.8}
.service-rule{height:1px;background:#c9d3de}
.check{display:flex;align-items:center;gap:8px;font-size:12.5px;color:var(--ink)}
.check svg{width:16px;height:16px;stroke:var(--text);fill:none;stroke-width:1.5;flex:none}
.service-card{left:457px;top:2074px;width:288px;height:277px;background:var(--white);border:2px solid var(--blue);box-shadow:0 10px 24px rgba(20,60,110,.12)}

/* Testimonials */
.avatar{left:362px;top:2709px;width:123px;height:97px;border-radius:50%;background:radial-gradient(circle at 55% 45%,#6a4a3c 0%,#c9b8ae 60%,#e7e1dd 100%)}
.quote-badge{left:378px;top:2744px;width:24px;height:24px;border-radius:50%;background:var(--orange);color:var(--white);font-size:14px;font-weight:600;display:flex;align-items:center;justify-content:center}
.testimonial-text{left:524px;top:2712px;width:365px;font-size:13px;line-height:28px;color:var(--text)}
.testimonial-name{left:524px;top:2818px;font-size:13px;color:var(--blue);font-weight:500}

/* News */
.news-card{width:261px}
.news-img{height:164px;position:relative}
.date{position:absolute;left:10px;top:12px;width:38px;height:38px;border-radius:50%;background:var(--white);font-size:8px;line-height:10px;text-align:center;display:flex;flex-direction:column;justify-content:center;color:var(--ink)}
.news-meta{font-size:9.5px;color:var(--blue);margin-top:20px;word-spacing:2px}
.news-meta span{margin-left:20px}
.news-title{font-size:15.5px;line-height:22px;font-weight:500;margin-top:6px}
.news-text{font-size:11.5px;line-height:21px;color:var(--muted);margin-top:8px}
.news-more{font-size:11.5px;color:var(--blue);font-weight:500;margin-top:8px;display:block}

/* Contact */
.contact-band{left:0;top:3470px;width:1200px;height:374px;background:#f0f3f7}
.contact-line1{top:3512px;font-size:26px;font-weight:300;color:var(--ink)}
.contact-line2{top:3552px;font-size:26px;font-weight:500}
.contact-line3{top:3602px;font-size:17px;font-weight:300;color:var(--text)}
.field{top:3664px;width:207px;height:33px;border:1px solid #c7cfd8;background:#f6f8fa;font-size:11.5px;color:var(--muted);padding:0 16px;display:flex;align-items:center}
.submit{left:544px;top:3731px;width:111px;height:37px}

/* Partners */
.partners{left:189px;top:3950px;width:824px;display:grid;grid-template-columns:repeat(4,1fr);grid-template-rows:100px 100px}
.partner{display:flex;align-items:center;justify-content:center}
.partner:nth-child(-n+4){border-bottom:1px solid var(--line)}
.partner:not(:nth-child(4n)){border-right:1px solid var(--line)}
.badge{width:130px;height:30px;border-radius:15px;background:#cfd4da}
.badge.sq{border-radius:4px;background:#b9c0c8}

/* Footer */
.footer{left:0;top:4206px;width:1200px;height:339px;background:var(--footer)}
.foot-h{font-size:12px;font-weight:600;color:var(--white);letter-spacing:.3px}
.foot-list{font-size:11px;line-height:24px;color:var(--footer-text)}
.foot-item{display:flex;gap:10px;font-size:11px;line-height:18px;color:var(--footer-text)}
.foot-item svg{width:14px;height:14px;stroke:var(--footer-text);fill:none;stroke-width:1.5;flex:none;margin-top:2px}
.subscribe{left:729px;top:4358px;width:282px;height:30px;display:flex}
.subscribe .in{flex:1;background:var(--white);border-radius:15px 0 0 15px;font-size:10px;color:var(--muted);display:flex;align-items:center;padding-left:20px}
.subscribe .go{width:102px;background:var(--orange);color:var(--white);border-radius:0 15px 15px 0;font-size:11px;font-weight:600;display:flex;align-items:center;justify-content:center}
.foot-rule{left:0;top:4483px;width:1200px;height:1px;background:rgba(255,255,255,.25)}
.copyright{left:189px;top:4503px;font-size:11px;color:var(--footer-text)}
.social{left:900px;top:4507px;display:flex;gap:8px}
.social i{width:9px;height:9px;border-radius:50%;background:var(--footer-text);display:block}
</style>
</head>
<body>

<!-- Hero -->
<svg class="hero-art" width="1200" height="740" viewBox="0 0 1200 740" role="img" aria-label="Bright blue hero photo of a hand touching a glowing digital padlock on a circuit background">
  <defs>
    <linearGradient id="heroFill" x1="0" y1="0" x2="1" y2="1">
      <stop offset="0" stop-color="#1b8ddc"/>
      <stop offset=".5" stop-color="#2e9fe8"/>
      <stop offset="1" stop-color="#1272c0"/>
    </linearGradient>
  </defs>
  <path d="M0 0H1200V575Q900 640 600 724Q300 640 0 582Z" fill="url(#heroFill)"/>
  <path d="M0 582Q300 640 600 724Q900 640 1200 575" fill="none" stroke="#8fcdf6" stroke-width="5"/>
</svg>

<div class="abs brand"><span class="brand-dot"></span>Quill Vantor</div>
<div class="abs topbar">
  <svg width="16" height="16" viewBox="0 0 24 24" fill="none" stroke="#fff" stroke-width="1.6"><path d="M5 3h4l2 5-3 2a11 11 0 0 0 6 6l2-3 5 2v4a2 2 0 0 1-2 2A17 17 0 0 1 3 5a2 2 0 0 1 2-2z"/></svg>
  <span>(000) 000-0000</span>
  <svg width="20" height="14" viewBox="0 0 20 14" fill="none" stroke="#fff" stroke-width="1.4" style="margin-left:22px"><rect x="1" y="1" width="18" height="12"/><path d="M1 1l9 7 9-7"/></svg>
  <a class="btn-quote" href="#">Get a quote</a>
</div>
<div class="abs nav-rule"></div>
<nav class="abs nav">
  <a href="#">Home</a><a href="#">How it works</a><a href="#">Products</a><a href="#">Pricing</a><a href="#">About Us</a><a href="#">Contact Us</a>
</nav>
<p class="abs hero-kicker">The Right People For Your Team.</p>
<h1 class="abs hero-title">Cyber Thrieats <span class="light">and</span><br>Digitalisation Risks</h1>
<a class="abs btn-start" href="#">GET STARTED</a>

<!-- About -->
<div class="abs about-visual" role="img" aria-label="Large network illustration on a soft grey dotted background"></div>
<p class="abs kicker about-kicker">About Company</p>
<h2 class="abs about-title">Improving Your<br>Security</h2>
<p class="abs about-text">Lorem Ipsum is simply dummy text of the printing and typesetting industry. Lorem Ipsum has been the industry's standard dummy text ever since the 1500s, when an unknown printer took a galley of type and scrambled</p>
<a class="abs btn about-btn" href="#">Learn More</a>

<!-- What we provide -->
<div class="abs provide-bg" role="img" aria-label="Faint light blue hexagon network pattern"></div>
<div class="abs section-head" style="top:1234px">
  <p class="label">About Company</p>
  <h2>What We Provide</h2>
  <div class="bar"></div>
</div>

<div class="abs hex-wrap" style="left:237px;top:1347px"><div class="hex">
  <svg viewBox="0 0 48 48"><circle cx="24" cy="24" r="18"/><path d="M16 24l6 6 11-12"/></svg>OUR SERVICES<div class="tick"></div></div></div>
<div class="abs hex-wrap" style="left:452px;top:1347px"><div class="hex">
  <svg viewBox="0 0 48 48"><path d="M14 32a8 8 0 0 1 1-16 11 11 0 0 1 21 3 7 7 0 0 1-1 13z"/><path d="M8 14a18 18 0 0 1 30-6M40 34a18 18 0 0 1-30 6"/></svg>OUR SERVICES<div class="tick"></div></div></div>
<div class="abs hex-wrap" style="left:667px;top:1347px"><div class="hex">
  <svg viewBox="0 0 48 48"><rect x="6" y="4" width="10" height="8"/><path d="M11 12v16M11 20h24v8"/><circle cx="11" cy="36" r="5"/><circle cx="24" cy="36" r="5"/><circle cx="37" cy="36" r="5"/><path d="M24 20v11"/></svg>OUR SERVICES<div class="tick"></div></div></div>

<div class="abs hex-wrap" style="left:345px;top:1529px"><div class="hex">
  <svg viewBox="0 0 48 48"><rect x="4" y="6" width="26" height="9" rx="2"/><rect x="4" y="18" width="26" height="9" rx="2"/><rect x="4" y="30" width="20" height="9" rx="2"/><circle cx="34" cy="34" r="10"/><path d="M24 34h20M34 24v20"/></svg>OUR SERVICES<div class="tick"></div></div></div>
<div class="abs hex-wrap" style="left:560px;top:1529px"><div class="hex active">
  <svg viewBox="0 0 48 48"><circle cx="24" cy="22" r="8"/><path d="M24 8v5M24 31v5M10 22h5M33 22h5M14 12l4 4M30 28l4 4M34 12l-4 4M18 28l-4 4"/><path d="M18 40h12"/></svg>OUR SERVICES<div class="tick"></div></div></div>
<div class="abs hex-wrap" style="left:775px;top:1529px"><div class="hex">
  <svg viewBox="0 0 48 48"><circle cx="24" cy="14" r="9"/><path d="M15 14h18M24 5c-4 5-4 13 0 18M24 5c4 5 4 13 0 18"/><rect x="4" y="28" width="12" height="16" rx="2"/><rect x="32" y="30" width="12" height="14" rx="2"/><path d="M16 36h16"/></svg>OUR SERVICES<div class="tick"></div></div></div>

<!-- Services -->
<svg class="abs" style="left:0;top:1820px" width="1200" height="820" viewBox="0 0 1200 820">
  <path d="M14 20Q300 -10 600 30T1200 0V520Q1000 600 700 690Q300 800 14 780Z" fill="#e3ebf6"/>
</svg>
<div class="abs section-head" style="top:1963px">
  <p class="label">Our business is divided in</p>
  <h2>Our Services</h2>
  <div class="bar"></div>
</div>

<div class="abs service-title" style="left:232px;top:2120px">
  <svg viewBox="0 0 48 48"><rect x="4" y="4" width="40" height="40"/><circle cx="24" cy="22" r="7"/><path d="M14 40h20M24 29v6"/></svg>Lorem Ipsum
</div>
<div class="abs service-rule" style="left:232px;top:2192px;width:186px"></div>
<div class="abs check" style="left:234px;top:2218px"><svg viewBox="0 0 16 16"><circle cx="8" cy="8" r="7"/><path d="M5 8l2 2 4-4"/></svg>Lorem Ipsum</div>
<div class="abs check" style="left:234px;top:2256px"><svg viewBox="0 0 16 16"><circle cx="8" cy="8" r="7"/><path d="M5 8l2 2 4-4"/></svg>Cloud Products</div>

<div class="abs service-card"></div>
<div class="abs service-title" style="left:505px;top:2120px">
  <svg viewBox="0 0 48 48"><circle cx="24" cy="22" r="14"/><circle cx="24" cy="22" r="5"/><path d="M24 8v6M24 30v6M10 22h6M32 22h6M18 40h12M20 44h8"/></svg>Professional<br>Services
</div>
<div class="abs service-rule" style="left:505px;top:2192px;width:186px"></div>
<div class="abs check" style="left:505px;top:2218px"><svg viewBox="0 0 16 16"><circle cx="8" cy="8" r="7"/><path d="M5 8l2 2 4-4"/></svg>Lorem Ipsum</div>
<div class="abs check" style="left:626px;top:2218px"><svg viewBox="0 0 16 16"><circle cx="8" cy="8" r="7"/><path d="M5 8l2 2 4-4"/></svg>Lorem Ipsum</div>
<a class="abs btn" href="#" style="left:541px;top:2270px;width:118px;height:36px">Learn More</a>

<div class="abs service-title" style="left:782px;top:2120px">
  <svg viewBox="0 0 48 48"><rect x="4" y="6" width="22" height="16" rx="2"/><circle cx="36" cy="12" r="6"/><path d="M22 44V30a3 3 0 0 1 6 0v6l8 2v6"/></svg>Managed<br>Services
</div>
<div class="abs service-rule" style="left:782px;top:2192px;width:186px"></div>
<div class="abs check" style="left:784px;top:2218px;align-items:flex-start;line-height:24px"><svg viewBox="0 0 16 16" style="margin-top:4px"><circle cx="8" cy="8" r="7"/><path d="M5 8l2 2 4-4"/></svg><span>responsible for services on<br>IT infrastructure of customer</span></div>

<!-- Testimonials -->
<div class="abs section-head" style="top:2602px">
  <p class="label">Our Customer Says</p>
  <h2>Testimonials</h2>
  <div class="bar"></div>
</div>
<div class="abs avatar" role="img" aria-label="Portrait photo of the customer"></div>
<div class="abs quote-badge">“</div>
<p class="abs testimonial-text">This is due to their excellent service, competitive pricing and customer support. It's throughly refresing to get such a personal touch.</p>
<p class="abs testimonial-name">Dana Morell</p>
<svg class="abs" style="left:850px;top:2848px" width="52" height="16" viewBox="0 0 52 16" fill="none" stroke-width="1.6">
  <path d="M20 8H2M8 2L2 8l6 6" stroke="#0b76c5"/><path d="M32 8h18M44 2l6 6-6 6" stroke="#9aa8b8"/>
</svg>

<!-- News -->
<div class="abs section-head" style="top:3005px"><h2>News and Articles</h2><div class="bar" style="background:var(--orange)"></div></div>

<article class="abs news-card" style="left:189px;top:3089px">
  <div class="news-img" role="img" aria-label="Photo of glowing blue digital padlock held in hands" style="background:linear-gradient(135deg,#1a5f8f,#3a9ad0 55%,#1d5c8a)"><div class="date"><b>30</b>Nov</div></div>
  <p class="news-meta">By Admin<span>2 Comments</span></p>
  <h3 class="news-title">Lorem Ipsum is simply dummy text of the printing</h3>
  <p class="news-text">There are many variations of passages of available but majority have alteration</p>
  <a class="news-more" href="#">Read More</a>
</article>
<article class="abs news-card" style="left:469px;top:3089px">
  <div class="news-img" role="img" aria-label="Photo of hand touching a transparent digital security screen" style="background:linear-gradient(135deg,#e9eef7,#9db6dc 55%,#5d7fb8)"><div class="date"><b>26</b>Nov</div></div>
  <p class="news-meta">By Admin<span>2 Comments</span></p>
  <h3 class="news-title">Lorem Ipsum is simply dummy text of the printing</h3>
  <p class="news-text">There are many variations of passages of available but majority have alteration</p>
  <a class="news-more" href="#">Read More</a>
</article>
<article class="abs news-card" style="left:752px;top:3089px">
  <div class="news-img" role="img" aria-label="Photo of businessman holding a glowing phone" style="background:linear-gradient(135deg,#2a5a99,#4a82c8 55%,#2a5a99)"><div class="date"><b>20</b>Nov</div></div>
  <p class="news-meta">By Admin<span>2 Comments</span></p>
  <h3 class="news-title">Lorem Ipsum is simply dummy text of the printing</h3>
  <p class="news-text">There are many variations of passages of available but majority have alteration</p>
  <a class="news-more" href="#">Read More</a>
</article>

<!-- Contact -->
<div class="abs contact-band"></div>
<p class="abs section-head contact-line1">We are always ahead</p>
<p class="abs section-head contact-line2">Professional Solutions for Your</p>
<p class="abs section-head contact-line3">I would like to discuss</p>
<div class="abs field" style="left:274px">Name</div>
<div class="abs field" style="left:496px">Email</div>
<div class="abs field" style="left:720px">Phone</div>
<a class="abs btn submit" href="#">Submit</a>

<!-- Partners -->
<div class="abs section-head" style="top:3875px"><h2>Our Partners</h2><div class="bar"></div></div>
<div class="abs partners">
  <div class="partner"><div class="badge"></div></div>
  <div class="partner"><div class="badge sq"></div></div>
  <div class="partner"><div class="badge"></div></div>
  <div class="partner"><div class="badge"></div></div>
  <div class="partner"><div class="badge"></div></div>
  <div class="partner"><div class="badge"></div></div>
  <div class="partner"><div class="badge"></div></div>
  <div class="partner"><div class="badge sq"></div></div>
</div>

<!-- Footer -->
<footer class="abs footer"></footer>
<p class="abs foot-h" style="left:189px;top:4268px">Contact Us</p>
<div class="abs foot-item" style="left:189px;top:4304px"><svg viewBox="0 0 16 16"><path d="M8 15s5-5 5-9A5 5 0 0 0 3 6c0 4 5 9 5 9z"/><circle cx="8" cy="6" r="2"/></svg><span>52 Orchard Lane #4<br>Austin 78701 TX</span></div>
<div class="abs foot-item" style="left:189px;top:4354px"><svg viewBox="0 0 24 24"><path d="M5 3h4l2 5-3 2a11 11 0 0 0 6 6l2-3 5 2v4a2 2 0 0 1-2 2A17 17 0 0 1 3 5a2 2 0 0 1 2-2z"/></svg><span>(000) 000 0000</span></div>
<div class="abs foot-item" style="left:189px;top:4394px"><svg viewBox="0 0 16 16"><rect x="1" y="3" width="14" height="10"/><path d="M1 3l7 6 7-6"/></svg><span>hello@quillvantor.com</span></div>

<p class="abs foot-h" style="left:439px;top:4268px">Quick Links</p>
<div class="abs foot-list" style="left:439px;top:4292px">Home<br>About Us<br>Services<br>How it works<br>Products</div>
<p class="abs foot-h" style="left:567px;top:4268px">Quick Links</p>
<div class="abs foot-list" style="left:567px;top:4292px">Pricing<br>Testimonials<br>Contact Us</div>

<p class="abs foot-h" style="left:738px;top:4268px">WRITE TO US</p>
<p class="abs foot-list" style="left:738px;top:4294px;line-height:20px;font-size:10px">Provide your email below to<br>subscribe to our newsletter</p>
<div class="abs subscribe"><div class="in">Email address</div><div class="go">Subscribe</div></div>

<div class="abs foot-rule"></div>
<p class="abs copyright">Copyright 2024 quillvantor.com</p>
<div class="abs social"><i></i><i></i><i></i><i></i><i></i></div>

</body>
</html>
```